Ironvale Holdings Business card

We need a an amazing matte black and gold card! W are a finance investing company so we want something that's eye catching and sleek. We want it to be attractive and sleek and represent money. Heck with would like the letters and lgo to be printed as 24k gold one day. We have the logo added so please use the color scheme with the logo and have that beautifully placed on one side.

Target Market(s)

Investors of all ages

Industry/Entity Type

Financial

Contact Information for Business Card

Black and matte with gold lettering follow logo colrs please.

Font styles to use
Other font styles liked:
• you decide

Colors

Designer to choose colors to be used in the design.

Requirements
Must have
• Matte Black and Gold, logo on one side. job title and name , website, phone number and email address on the other side
Nice to have
• Matte black and crisp finish to attract investors
Should not have
• playful, very professional!

```html
<!DOCTYPE html>
<html lang="en">
<head>
<meta charset="utf-8">
<title>Ironvale Holdings Business Card</title>
<link href="https://fonts.googleapis.com/css2?family=Montserrat:wght@400;500;600&display=swap" rel="stylesheet">
<style>
  :root {
    --backdrop: #2b2725;
    --card-black: #0d0d0d;
    --gold: #d4b22c;
    --gold-line: #b99a22;
    --text-light: #e8e6e1;
  }
  * { box-sizing: border-box; margin: 0; padding: 0; }
  html, body {
    width: 1200px;
    height: 716px;
    overflow: hidden;
    background: var(--backdrop);
    font-family: "Montserrat", sans-serif;
  }
  .stage {
    width: 1200px;
    height: 716px;
    display: flex;
    align-items: center;
    justify-content: center;
    gap: 48px;
  }
  .card {
    position: relative;
    width: 532px;
    height: 304px;
    background: var(--card-black);
    box-shadow: 0 10px 30px rgba(0,0,0,0.45);
  }
  .wordmark {
    color: var(--gold);
    font-weight: 500;
    text-transform: uppercase;
    letter-spacing: 0.12em;
    white-space: nowrap;
  }
  .card-front .wordmark {
    position: absolute;
    left: 50%;
    top: 42%;
    transform: translate(-50%, -50%);
    font-size: 28px;
  }
  .card-back .wordmark {
    position: absolute;
    left: 150px;
    top: 40px;
    font-size: 17px;
  }
  .identity {
    position: absolute;
    left: 56px;
    top: 118px;
  }
  .identity .name {
    color: var(--gold);
    font-weight: 600;
    font-size: 15px;
  }
  .identity .title {
    color: var(--text-light);
    font-size: 11px;
    margin-top: 2px;
  }
  .rule {
    position: absolute;
    left: 150px;
    right: 48px;
    top: 158px;
    height: 1px;
    background: var(--gold-line);
  }
  .contacts {
    position: absolute;
    left: 40px;
    top: 172px;
    list-style: none;
  }
  .contacts li {
    display: flex;
    align-items: center;
    gap: 8px;
    color: var(--text-light);
    font-size: 11.5px;
    line-height: 20px;
  }
  .contacts svg { width: 9px; height: 9px; flex: none; }
</style>
</head>
<body>
  <main class="stage">
    <section class="card card-front" aria-label="Card front">
      <p class="wordmark">Ironvale Holdings</p>
    </section>

    <section class="card card-back" aria-label="Card back">
      <p class="wordmark">Ironvale Holdings</p>
      <div class="identity">
        <p class="name">Daniel Marsh</p>
        <p class="title">Director</p>
      </div>
      <div class="rule"></div>
      <ul class="contacts">
        <li>
          <svg viewBox="0 0 10 10" aria-hidden="true"><path d="M2 1 L4 1 L4.6 3 L3.4 3.8 Q4.6 6 6.2 6.6 L7 5.4 L9 6 L9 8 Q5 9 2.2 5.8 Q0.8 3.5 2 1Z" fill="var(--gold)"/></svg>
          613-555-0142
        </li>
        <li>
          <svg viewBox="0 0 10 10" aria-hidden="true"><rect x="0.5" y="2" width="9" height="6" fill="var(--gold)"/><path d="M0.5 2 L5 5.5 L9.5 2" stroke="var(--card-black)" stroke-width="0.9" fill="none"/></svg>
          info@ironvaleholdings.com
        </li>
        <li>
          <svg viewBox="0 0 10 10" aria-hidden="true"><circle cx="5" cy="5" r="4.5" fill="var(--gold)"/><path d="M0.5 5 H9.5 M5 0.5 Q2.5 5 5 9.5 M5 0.5 Q7.5 5 5 9.5" stroke="var(--card-black)" stroke-width="0.7" fill="none"/></svg>
          www.ironvaleholdings.com
        </li>
      </ul>
    </section>
  </main>
</body>
</html>
```